Homepage design for Dutch Job Posting Site (Vakmeld.nl)

We need a redesign of our homepage www.Vakmeld.nl to make it very clear what we do. We are an online job posting portal and are looking to recruit clients and professionals on a single page.

The Homepage will focus on CLIENTS (OPDRACHTGEVERS), with the idea that if we have a lot of jobs posted, then the professionals will come.

Important to know is that we now have ONE REGISTRATION for both professionals and clients - so there is no need for two separate registration options.

Also important to know is that the JOB POSTER pages will have a GREEN hyperlinks color (see the color above the OPDRACHTGEVER at the top of the screen) and the Professionals will have a BLUE hyperlinks color (see the color above the PROFESSIONAL at the top of the screen).

At the top of the page, we would like a 4 page slider (we will do the coding but just want 4 slides) that shows how it works and what makes us unique. In the examples below, you can see that we have already done 2 of them, and we will ask the designer to help do the other two once the project is awarded.

You can see from the images provided that we have already done most of the work. The HEADER WRAP and the FOOTER are already done, and you can use these in your examples.

Notice also in the image "Homepage-BannerBlank" the image used in the center. It is an image that is only as wide as the header and then fades off into a background image that we can use repeat-x in the css of the site which fills the screen on any monitor resolution. If you don't understand what I just wrote, you probably are not the right designer for the job.

Notice also that the two images "NU AANMELDEN" and "VAKMELD ESCROW" use background images that have a SUBTLE background image - it is not just a gradient color change. This is what we LOVE in the design so far.

You can see that our design is already very far advanced, so what we are looking for in a new design are not the overall redesign, but specific, subtle design improvements to give the page a CLEAN, FRESH, MODERN look without being busy and crowded.

Where we specifically want help is in these areas. The designers that show us these elements will be the ones selected. All others will be eliminated without further comment:
a) How to blend in the Vakmeld logo into the header design without taking up more HEIGHT (we have done a white overlay, but this is where you can prove to us that you are great.

b) We need a font for our h1 tags in our site. This will be the same font used in "Laatste Opdrachten" "Laatste Blogs" "Zoek uw professional per categorie of rubriek". Do not use a webfont (Arial or Verdana). Instead, refer to the examples provided for inspiration of a font that best suits the site for a header.

c) We need better containers for "Laatse opdrachten", "Laatste Blogs" and Zoek uw professional per categorie of rubriek. They can have colors or just borders or just outlines. They should compliment the site look though and not distract from it.

d) Transitions between the containers and other elements. Right now they are all just boxy and separate, but there could be some overlap, some shadows, an image divider (as there is between "Laatste Blogs" and TornQX) but again, the transitions need top complement the design and not take it over.

Sites that appeal to us for what we are looking for are:
- plumvo.com
- www.ferlindo.com*
- Marblequist.com*
- Tindelvane.com*
*What we like here are both the top PROMINENT central message and then the smaller subtler design transitions underneath.

Feel free to use images or icons to complement the look, but it must be clean, fresh and modern.

Target Market(s)

University-educated Job Posters between 18 - 45

Industry/Entity Type

Online

Requirements
Must have
• - The header wrapper height but be exactly as it is on the images given. This header will be used on all the inner pages and therefore cannot be any higher than what is shown.
- Focus on the 4 tasks outlined
- Keep it clean! We love white, but also like small icons where appropriate and clean transitions.
Nice to have
• Dutch text is NOT important, we can translate.
Should not have
• No cluttered design.

```html
<!DOCTYPE html>
<html lang="nl">
<head>
<meta charset="utf-8">
<title>Vakmeld – Homepage</title>
<link href="https://fonts.googleapis.com/css2?family=Ubuntu:wght@400;500;700&family=Open+Sans:wght@400;600&display=swap" rel="stylesheet">
<style>
:root{
  --green:#8cc20f;
  --green-dark:#5e9a05;
  --green-band:#7db514;
  --link-green:#82b800;
  --text:#333;
  --muted:#8a8a8a;
  --grey-btn:#c9c9c9;
  --dark-btn:#4a4a4a;
  --border:#e2e2e2;
}
*{box-sizing:border-box;margin:0;padding:0}
html,body{width:1010px;height:1200px;overflow:hidden}
body{position:relative;background:#fff;font-family:"Open Sans",Arial,sans-serif;color:var(--text)}
.abs{position:absolute}

/* header */
.site-header{left:0;top:0;width:1010px;height:147px;background:linear-gradient(#f2f2f2,#fafafa 40%,#e9e9e9);border-bottom:1px solid #c8c8c8}
.brand{left:100px;top:40px;display:flex;align-items:center;gap:8px}
.brand-dot{width:22px;height:22px;border-radius:50%;background:var(--green)}
.brand-name{font-family:"Ubuntu",sans-serif;font-weight:700;font-size:34px;color:#3d3d3d;line-height:1}
.role-btn{top:48px;height:29px;border-radius:3px;font-family:"Ubuntu",sans-serif;font-weight:700;font-size:11.5px;color:#fff;display:flex;align-items:center;justify-content:center;letter-spacing:.3px}
.role-client{left:333px;width:112px;background:linear-gradient(#a4d52a,var(--green-dark));border:2px solid #b9e24a}
.role-pro{left:453px;width:111px;background:linear-gradient(#e2e2e2,var(--grey-btn));border:2px solid #ddd}
.follow{left:730px;top:60px;font-size:11.5px;color:#666;display:flex;align-items:center;gap:4px}
.follow span.sq{width:20px;height:20px;border-radius:3px;background:#9bb3c7;display:inline-block}
.follow span.first{margin-left:4px}
.main-nav{left:110px;top:118px;display:flex;gap:23px;font-size:13.5px;color:#555}
.main-nav a{color:#555;text-decoration:none;border-bottom:1px solid #c8e28a;padding-bottom:2px}
.account{left:764px;top:124px;font-size:11.5px;color:#444}
.account-icons{left:780px;top:100px;display:flex;gap:46px}
.account-icons i{width:16px;height:18px;display:block;border-radius:3px;background:#6b9bc6}
.account-icons i:first-child{background:#7aa63a}

/* slider */
.slider{left:104px;top:156px;width:774px;height:249px;background:linear-gradient(#fff,#f6f6f6);border:1px solid #e5e5e5;box-shadow:0 2px 4px rgba(0,0,0,.12)}
.slide-visual{left:125px;top:170px;width:240px;height:232px;background:linear-gradient(135deg,#eef3f7,#9ccbe8 60%,#6fbe2c);}
.slide-title{left:397px;top:166px;width:203px;height:38px;background:linear-gradient(#9ad61c,#7cc10a);border:2px solid #b6e44a;font-family:"Ubuntu",sans-serif;font-weight:700;font-size:20px;color:#fff;display:flex;align-items:center;justify-content:center}
.slide-text{left:398px;top:222px;width:460px;font-size:12.5px;line-height:15.5px;color:#777}
.slide-text p+p{margin-top:15px}
.btn-dark{background:linear-gradient(#777,#3e3e3e);color:#fff;border-radius:3px;font-weight:600;display:flex;align-items:center;justify-content:center}
.read-more{left:724px;top:361px;width:111px;height:29px;font-size:11.5px;border:1px solid #333}
.slide-arrow{top:337px;width:22px;height:40px;background:#ddd;display:flex;align-items:center;justify-content:center}
.arrow-left{left:82px;border-radius:20px 0 0 20px}
.arrow-right{left:878px;border-radius:0 20px 20px 0}
.slide-dots{left:398px;top:405px;width:198px;height:27px;background:linear-gradient(#eee,#c9c9c9);border-radius:0 0 60px 60px;display:flex;justify-content:center;align-items:center;gap:7px}
.slide-dots i{width:16px;height:16px;border-radius:50%;background:#ccc;border:1px solid #aaa;display:block}
.slide-dots i.on{background:radial-gradient(#888 30%,#eee 35%)}

/* search band */
.search-band{left:0;top:441px;width:1010px;height:147px;background:linear-gradient(#86c316,#6ea810)}
.search-title{font-family:"Ubuntu",sans-serif;font-weight:500;font-size:17.5px;color:#fff;top:462px}
.people-icon{left:32px;top:456px;width:60px;height:54px;border-radius:8px;background:linear-gradient(#6b9fd8,#d36a5a)}
.search-input{top:493px;height:28px;background:#fff;border:1px solid #ddd;border-radius:2px;font-size:11px;color:#888;padding:8px 7px 0}
.search-select{top:493px;height:28px;background:#fff;border:1px solid #ddd;border-radius:2px;font-size:10.5px;color:#333;padding:7px 5px 0}
.search-select svg{position:absolute;right:6px;top:10px}
.search-btn{top:493px;height:28px;background:linear-gradient(#7aae12,#4e8408);border:1px solid #a8d64a;color:#fff;font-family:"Ubuntu",sans-serif;font-weight:700;font-size:11px;display:flex;align-items:center;justify-content:center;border-radius:2px}
.search-hint{top:525px;font-size:8.5px;color:#fff}
.promo{left:190px;top:555px;font-family:"Open Sans",sans-serif;font-style:italic;font-weight:600;font-size:16.5px;color:#fff}
.post-btn{left:602px;top:556px;width:124px;height:19px;font-size:10.5px;font-weight:400;border:1px solid #bbb}

/* latest jobs */
.jobs{left:104px;top:598px;width:774px;height:539px;background:#fff;border:1px solid #e6e6e6;box-shadow:0 2px 4px rgba(0,0,0,.1)}
.jobs-head{left:118px;top:608px;font-family:"Ubuntu",sans-serif;font-weight:700;font-size:17px;color:#333}
.see-all{font-size:11px;color:#222;text-decoration:underline}
.job-row{left:105px;width:772px;height:76px;background:linear-gradient(#fff,#f7f7f7);border-top:1px solid #f0f0f0}
.job-title{position:absolute;left:11px;top:7px;font-family:"Ubuntu",sans-serif;font-weight:700;font-size:14px;color:var(--link-green)}
.job-title em{font-style:normal;color:#666;font-weight:400;margin:0 3px}
.job-title u{font-size:10px}
.job-desc{position:absolute;left:12px;top:32px;width:570px;font-size:11.2px;line-height:13.6px;color:#333}
.job-days{position:absolute;left:644px;top:11px;font-size:11.5px;color:var(--muted)}
.job-link{position:absolute;left:646px;top:38px;font-size:11.5px;color:var(--link-green);text-decoration:underline;display:flex;align-items:center;gap:6px}
.jobs-foot{left:105px;top:1096px;width:772px;height:40px;background:linear-gradient(#f4f4f4,#fbfbfb)}

/* footer */
.site-footer{left:0;top:1144px;width:1010px;height:56px;background:linear-gradient(#86c316,#6ea810)}
.footer-nav{left:106px;top:1165px;font-size:10.5px;color:#fff}
.footer-brand{left:760px;top:1158px;display:flex;align-items:center;gap:6px}
.footer-brand .brand-dot{width:14px;height:14px}
.footer-brand .brand-name{font-size:25px;color:#2f4d0a}
</style>
</head>
<body>

<header class="site-header abs">
</header>
<div class="brand abs"><span class="brand-dot"></span><span class="brand-name">Vakmeld</span></div>
<div class="role-btn role-client abs">OPDRACHTGEVER</div>
<div class="role-btn role-pro abs">PROFESSIONAL</div>
<div class="follow abs">Follow us <span class="sq first"></span><span class="sq"></span><span class="sq"></span><span class="sq"></span></div>
<nav class="main-nav abs"><a>Home</a><a>Opdrachten</a><a>Mijn Kantoor</a><a>Hoe het werkt</a><a>Blog</a></nav>
<div class="account-icons abs"><i></i><i></i></div>
<div class="account abs">Aanmelden | Inloggen</div>

<section class="slider abs"></section>
<div class="slide-visual abs" role="img" aria-label="Illustratie: zakenmensen op een groeiende grafiek"></div>
<div class="slide-title abs">How it works ?</div>
<div class="slide-text abs">
  <p>Op Vakmeld.nl kunt u met 1 account zowel opdrachten uitvoeren als plaatsen. De werkruimten van beide 'rollen' op de website zijn gescheiden om het overzicht goed te kunnen bewaren.</p>
  <p>U kunt altijd zien of u als opdrachtgever of als professional op de website bent ingelogd. Bent u namelijk ingelogd als opdrachtgever dan is het menu groen en wanneer u als professional bent ingelogd is het menu blauw.</p>
</div>
<div class="read-more btn-dark abs">Lees meer</div>
<div class="slide-arrow arrow-left abs"><svg width="10" height="14"><path d="M9 1L2 7l7 6z" fill="#fff"/></svg></div>
<div class="slide-arrow arrow-right abs"><svg width="10" height="14"><path d="M1 1l7 6-7 6z" fill="#fff"/></svg></div>
<div class="slide-dots abs"><i></i><i class="on"></i><i></i><i></i></div>

<section class="search-band abs"></section>
<div class="people-icon abs" role="img" aria-label="Icoon van twee professionals"></div>
<div class="search-title abs" style="left:95px">Zoek Professionals</div>
<div class="search-input abs" style="left:99px;width:186px">Vul hier uw zoekopdracht in ...</div>
<div class="search-select abs" style="left:291px;width:109px">Alle Categorieen<svg width="11" height="9"><path d="M0 0h11L5.5 9z" fill="#555"/></svg></div>
<div class="search-btn abs" style="left:406px;width:63px">ZOEKEN</div>
<div class="search-hint abs" style="left:102px">De juiste Professional vinden voor uw opdracht</div>

<svg class="abs" style="left:532px;top:452px" width="56" height="56" viewBox="0 0 56 56"><circle cx="34" cy="22" r="15" fill="#cfe6f7" stroke="#777" stroke-width="4"/><path d="M23 33L6 50" stroke="#333" stroke-width="7" stroke-linecap="round"/></svg>
<div class="search-title abs" style="left:596px">Zoek Opdrachten</div>
<div class="search-input abs" style="left:600px;width:187px">Vul hier uw zoekopdracht in ...</div>
<div class="search-select abs" style="left:793px;width:108px">Alle Categorieen<svg width="11" height="9"><path d="M0 0h11L5.5 9z" fill="#555"/></svg></div>
<div class="search-btn abs" style="left:907px;width:64px">ZOEKEN</div>
<div class="search-hint abs" style="left:604px">Verdien geld door de juiste Opdracht te vinden</div>

<div class="promo abs">Wilt u dat professionals vechten om uw opdracht?</div>
<div class="post-btn btn-dark abs">Opdracht Plaatsen &gt;&gt;</div>

<section class="jobs abs"></section>
<h1 class="jobs-head abs">Laatste Opdrachten</h1>
<a class="see-all abs" style="left:765px;top:609px">Alles Bekijken</a>

<div class="job-row abs" style="top:640px"><div class="job-title">VOIP telefonie in kantoor instellen<em>|</em><u>Category IT</u></div><p class="job-desc">Voor mijn kantoor tot 5 werkplekken ben ik op zoek naar een bedrijf dat de telefonie voor mij op de juiste wijze kan instellen. Ik heb een Belvox online nummer, wat het vaste telefoonnummer moet worden, waarop alle medewerkers te bereiken zijn. Verder moet er doorverbonden kunnen worden naar specifi....</p><span class="job-days">13 gaden delegen</span><a class="job-link">Opdracht bekijken <svg width="10" height="10"><circle cx="5" cy="5" r="4.5" fill="#eef" stroke="#bcd"/><path d="M4 3l2 2-2 2" stroke="#6a9" fill="none"/></svg></a></div>
<div class="job-row abs" style="top:716px"><div class="job-title">VOIP telefonie in kantoor instellen<em>|</em><u>Category IT</u></div><p class="job-desc">Voor mijn kantoor tot 5 werkplekken ben ik op zoek naar een bedrijf dat de telefonie voor mij op de juiste wijze kan instellen. Ik heb een Belvox online nummer, wat het vaste telefoonnummer moet worden, waarop alle medewerkers te bereiken zijn. Verder moet er doorverbonden kunnen worden naar specifi....</p><span class="job-days">13 gaden delegen</span><a class="job-link">Opdracht bekijken <svg width="10" height="10"><circle cx="5" cy="5" r="4.5" fill="#eef" stroke="#bcd"/><path d="M4 3l2 2-2 2" stroke="#6a9" fill="none"/></svg></a></div>
<div class="job-row abs" style="top:792px"><div class="job-title">VOIP telefonie in kantoor instellen<em>|</em><u>Category IT</u></div><p class="job-desc">Voor mijn kantoor tot 5 werkplekken ben ik op zoek naar een bedrijf dat de telefonie voor mij op de juiste wijze kan instellen. Ik heb een Belvox online nummer, wat het vaste telefoonnummer moet worden, waarop alle medewerkers te bereiken zijn. Verder moet er doorverbonden kunnen worden naar specifi....</p><span class="job-days">13 gaden delegen</span><a class="job-link">Opdracht bekijken <svg width="10" height="10"><circle cx="5" cy="5" r="4.5" fill="#eef" stroke="#bcd"/><path d="M4 3l2 2-2 2" stroke="#6a9" fill="none"/></svg></a></div>
<div class="job-row abs" style="top:868px"><div class="job-title">VOIP telefonie in kantoor instellen<em>|</em><u>Category IT</u></div><p class="job-desc">Voor mijn kantoor tot 5 werkplekken ben ik op zoek naar een bedrijf dat de telefonie voor mij op de juiste wijze kan instellen. Ik heb een Belvox online nummer, wat het vaste telefoonnummer moet worden, waarop alle medewerkers te bereiken zijn. Verder moet er doorverbonden kunnen worden naar specifi....</p><span class="job-days">13 gaden delegen</span><a class="job-link">Opdracht bekijken <svg width="10" height="10"><circle cx="5" cy="5" r="4.5" fill="#eef" stroke="#bcd"/><path d="M4 3l2 2-2 2" stroke="#6a9" fill="none"/></svg></a></div>
<div class="job-row abs" style="top:944px"><div class="job-title">VOIP telefonie in kantoor instellen<em>|</em><u>Category IT</u></div><p class="job-desc">Voor mijn kantoor tot 5 werkplekken ben ik op zoek naar een bedrijf dat de telefonie voor mij op de juiste wijze kan instellen. Ik heb een Belvox online nummer, wat het vaste telefoonnummer moet worden, waarop alle medewerkers te bereiken zijn. Verder moet er doorverbonden kunnen worden naar specifi....</p><span class="job-days">13 gaden delegen</span><a class="job-link">Opdracht bekijken <svg width="10" height="10"><circle cx="5" cy="5" r="4.5" fill="#eef" stroke="#bcd"/><path d="M4 3l2 2-2 2" stroke="#6a9" fill="none"/></svg></a></div>
<div class="job-row abs" style="top:1020px"><div class="job-title">VOIP telefonie in kantoor instellen<em>|</em><u>Category IT</u></div><p class="job-desc">Voor mijn kantoor tot 5 werkplekken ben ik op zoek naar een bedrijf dat de telefonie voor mij op de juiste wijze kan instellen. Ik heb een Belvox online nummer, wat het vaste telefoonnummer moet worden, waarop alle medewerkers te bereiken zijn. Verder moet er doorverbonden kunnen worden naar specifi....</p><span class="job-days">13 gaden delegen</span><a class="job-link">Opdracht bekijken <svg width="10" height="10"><circle cx="5" cy="5" r="4.5" fill="#eef" stroke="#bcd"/><path d="M4 3l2 2-2 2" stroke="#6a9" fill="none"/></svg></a></div>

<div class="jobs-foot abs"></div>
<a class="see-all abs" style="left:765px;top:1110px">Alles Bekijken</a>

<footer class="site-footer abs"></footer>
<div class="footer-nav abs">Home &nbsp;|&nbsp; Opdrachten &nbsp;|&nbsp; Mijn Kantoor &nbsp;|&nbsp; Hoe het werkt &nbsp;|&nbsp; Blog</div>
<div class="footer-brand abs"><span class="brand-dot"></span><span class="brand-name">Vakmeld</span></div>

</body>
</html>
```